Renewable energy website needs a wordpress website

We are a Renewable Energy company specialising in Energy Management, LED Lights and Solar PV Systems based in Kuala Lumpur.
We need wordpress website designed to match our company identity.
We would like to stick with similar shades of blue & green as our logo and to keep it fresh and creative at the same time.

It Company

```html
<!DOCTYPE html>
<html lang="en">
<head>
<meta charset="utf-8">
<title>Brightwell Energy</title>
<link href="https://fonts.googleapis.com/css2?family=Cabin:wght@400;500;600&family=Open+Sans:wght@400;600&display=swap" rel="stylesheet">
<style>
:root{
  --blue:#1c86dc;
  --blue-deep:#0d66c4;
  --blue-light:#3aa1ef;
  --blue-text:#2b8fd8;
  --green:#5aa526;
  --green-dark:#3f8a16;
  --paper:#f1f1f1;
  --grey-text:#8a8a8a;
  --line:#cfcfcf;
  --footer:#3a3a3a;
  --footer-bar:#2a2a2a;
  --footer-text:#d8d8d8;
  --white:#ffffff;
}
*{margin:0;padding:0;box-sizing:border-box}
html,body{width:794px;height:1200px;overflow:hidden}
body{position:relative;background:var(--paper);font-family:"Open Sans",sans-serif;color:var(--grey-text)}
.abs{position:absolute}

.top-rule{left:0;top:0;width:794px;height:3px;background:#444}
.header{left:0;top:3px;width:794px;height:65px;background:var(--paper)}
.brand{left:48px;top:17px;display:flex;align-items:center;gap:8px}
.brand-dot{width:34px;height:34px;border-radius:50%;background:var(--blue)}
.brand-name{font-family:"Cabin",sans-serif;font-weight:600;font-size:15px;color:var(--blue);letter-spacing:1px;line-height:1}
.social-top{left:504px;top:24px;display:flex;gap:4px}
.social-top span{width:19px;height:19px;border-radius:50%;background:#2f6fb0}
.search{left:580px;top:24px;width:128px;height:22px;border:1px solid #cfcfcf;background:#fff;font-size:7px;color:#aaa;padding:6px 6px;letter-spacing:.5px}
.search-btn{left:677px;top:24px;width:31px;height:22px;background:var(--blue)}

.nav{left:0;top:68px;width:794px;height:34px;background:linear-gradient(#3fa4f2,#1b7fd9)}
.nav ul{list-style:none;display:flex;height:34px;padding-left:47px}
.nav li{font-family:"Cabin",sans-serif;font-size:11.5px;letter-spacing:1px;color:var(--white);line-height:34px;padding:0 8px;margin-right:14px}
.nav li.active{background:#5fb6f5}

.hero-photo{left:0;top:102px;width:794px;height:308px;background:linear-gradient(160deg,#5d7fa6,#1f4a78 55%,#4f7aa3)}
.hero-panel{left:0;top:147px;width:794px;height:197px;background:linear-gradient(90deg,#1573d3,#1e7fd8 60%,#2a87dc)}
.hero-circle{left:106px;top:134px;width:230px;height:230px;border-radius:50%;border:6px solid #fff;background:radial-gradient(circle at 50% 45%,#eaf6ff,#8ccdf5 60%,#45a5e6)}
.hero-copy{left:399px;top:171px;width:300px;color:var(--white)}
.hero-copy h1{font-family:"Cabin",sans-serif;font-weight:500;font-size:13.5px;letter-spacing:1.6px;margin-bottom:6px}
.hero-copy p{font-size:9px;line-height:13.4px;letter-spacing:.3px}
.btn{display:inline-block;height:22px;line-height:20px;font-size:7.5px;letter-spacing:.8px;color:#fff;text-align:center;margin-top:9px}
.btn-outline{width:91px;border:1px solid #cfe6fb;margin-right:5px}
.btn-green{width:104px;background:linear-gradient(#6ebd2c,var(--green-dark));border:1px solid #4c9a1c}

.offer-title{left:0;top:434px;width:794px;text-align:center;font-family:"Cabin",sans-serif;font-size:15.5px;letter-spacing:2px;color:var(--blue-text)}
.offer-title em{font-style:normal;color:var(--green)}
.offer-rule{left:90px;top:468px;width:616px;height:1px;background:var(--line)}
.offer-dot{left:389px;top:462px;width:14px;height:14px;border-radius:50%;background:var(--blue-light)}

.card{width:190px}
.card-frame{width:188px;height:114px;background:#e4e4e4;padding:5px}
.card-photo{width:100%;height:100%}
.card h3{font-family:"Cabin",sans-serif;font-weight:500;font-size:11.5px;letter-spacing:1px;color:var(--blue-text);margin:10px 0 1px 5px}
.card p{font-size:9px;line-height:13.3px;letter-spacing:.3px;margin-left:5px;width:190px}

.about-band{left:0;top:727px;width:794px;height:192px;background:linear-gradient(#1c7fd4,#2c93e0 50%,#1f85d8)}
.about-frame{left:121px;top:755px;width:254px;height:142px;background:#5aaef0;padding:4px}
.about-photo{width:100%;height:100%;background:linear-gradient(135deg,#e8eef3,#cdd9e3 60%,#dfe7ee)}
.about-copy{left:401px;top:757px;width:290px;color:var(--white)}
.about-copy h2{font-family:"Cabin",sans-serif;font-weight:500;font-size:17px;margin-bottom:5px}
.about-copy p{font-size:8.8px;line-height:13.4px;text-align:justify;margin-bottom:13px}

.partners{left:0;top:919px;width:794px;height:138px;background:linear-gradient(#f0f0f0,#dcdcdc)}
.badge{position:absolute;background:#4a4a4a}

.footer{left:0;top:1057px;width:794px;height:115px;background:linear-gradient(#474747,var(--footer))}
.footer h4{font-family:"Cabin",sans-serif;font-weight:500;font-size:11.5px;letter-spacing:1.4px;color:#eee;margin-bottom:6px}
.footer p,.footer li{font-size:7.4px;line-height:9.5px;letter-spacing:1px;color:var(--footer-text);list-style:none}
.footer-social{display:flex;gap:4px}
.footer-social span{width:19px;height:19px;border-radius:50%;background:#f0f0f0}
.footer-bar{left:0;top:1172px;width:794px;height:28px;background:var(--footer-bar);font-size:7.4px;letter-spacing:1px;color:var(--footer-text);line-height:28px}
</style>
</head>
<body>
<div class="abs top-rule"></div>

<header class="abs header">
  <div class="abs brand"><span class="brand-dot"></span><span class="brand-name">BRIGHTWELL ENERGY</span></div>
  <div class="abs social-top"><span></span><span></span><span></span></div>
  <div class="abs search">Keyword Search</div>
  <div class="abs search-btn">
    <svg width="31" height="22" viewBox="0 0 31 22"><circle cx="13" cy="9.5" r="4.5" fill="none" stroke="#fff" stroke-width="2"/><line x1="16.5" y1="13" x2="21" y2="17" stroke="#fff" stroke-width="2.5" stroke-linecap="round"/></svg>
  </div>
</header>

<nav class="abs nav">
  <ul>
    <li class="active">HOME</li><li>ABOUT US</li><li>OUR SERVICES</li><li>OUR PRODUCTS</li><li>TECHNOLOGIES</li><li>CONTACT US</li>
  </ul>
</nav>

<section>
  <div class="abs hero-photo" role="img" aria-label="Photo of a solar panel field under a blue sky"></div>
  <div class="abs hero-panel"></div>
  <div class="abs hero-circle" role="img" aria-label="Illustration of hands holding a green island with wind turbines, a city and a solar panel"></div>
  <div class="abs hero-copy">
    <h1>WELCOME TO BRIGHTWELL ENERGY</h1>
    <p>Lorem ipsum dolor sit amet, consectetur adipiscing elit. Phasellus pulvinar sollicitudin elit sit amet euismod. Vestibulum ut vehicula lectus. Donec vulputate orci quis massa fringilla, non euismod sapien fermentum. Nam nec ligula magna. Sed ultrices justo sit amet mauris ullamcorper pharetra vitae id dui. Ut eros augue, egestas quis nulla iaculis, fringilla molestie tellus. Donec massa orci, tincidunt eget tellus in, molestie commodo urna.</p>
    <span class="btn btn-outline">Read more</span><span class="btn btn-green">Get a free Quote</span>
  </div>
</section>

<section>
  <h2 class="abs offer-title">WHAT <em>WE</em> OFFER</h2>
  <div class="abs offer-rule"></div>
  <div class="abs offer-dot"></div>

  <article class="abs card" style="left:90px;top:496px">
    <div class="card-frame"><div class="card-photo" role="img" aria-label="Photo of a worker installing solar panels on a house roof" style="background:linear-gradient(160deg,#b9c7cf,#7f8f6e 45%,#2a3a5a)"></div></div>
    <h3>Residential Solar Power</h3>
    <p>Lorem ipsum dolor sit amet, consectetur adipiscing elit. Phasellus pulvinar sollicitudin elit sit amet euismod. Vestibulum ut vehicula lectus.</p>
  </article>
  <article class="abs card" style="left:305px;top:496px">
    <div class="card-frame"><div class="card-photo" role="img" aria-label="Rendering of solar canopies over a car park" style="background:linear-gradient(170deg,#8fb6dc,#4f6b8a 40%,#6f7a7a 70%,#5b8a4a)"></div></div>
    <h3>Commercial Solar Power</h3>
    <p>Lorem ipsum dolor sit amet, consectetur adipiscing elit. Phasellus pulvinar sollicitudin elit sit amet euismod. Vestibulum ut vehicula lectus.</p>
  </article>
  <article class="abs card" style="left:518px;top:496px">
    <div class="card-frame"><div class="card-photo" role="img" aria-label="Photo of rows of glowing LED bulbs" style="background:radial-gradient(circle at 60% 60%,#8a7dff,#3a3fc9 55%,#101a5a)"></div></div>
    <h3>LED Lighting</h3>
    <p>Lorem ipsum dolor sit amet, consectetur adipiscing elit. Phasellus pulvinar sollicitudin elit sit amet euismod. Vestibulum ut vehicula lectus.</p>
  </article>
</section>

<section>
  <div class="abs about-band"></div>
  <div class="abs about-frame"><div class="about-photo" role="img" aria-label="Faded photo of technicians working on a solar array"></div></div>
  <div class="abs about-copy">
    <h2>ABOUT US</h2>
    <p>Lorem ipsum dolor sit amet, consectetur adipiscing elit. Phasellus pulvinar sollicitudin elit sit amet euismod. Vestibulum ut vehicula lectus. Donec vulputate orci quis massa fringilla, non euismod sapien fermentum. Nam nec ligula magna.</p>
    <p>Sed ultrices justo sit amet mauris ullamcorper pharetra vitae id dui. Ut eros augue, egestas quis nulla iaculis, fringilla molestie tellus. Donec massa orci, tincidunt eget tellus in, molestie commodo urna.</p>
  </div>
</section>

<section class="abs partners" aria-label="Partners and accreditations">
  <span class="badge" style="left:121px;top:43px;width:57px;height:57px;border-radius:50%"></span>
  <span class="badge" style="left:222px;top:46px;width:34px;height:52px;border-radius:4px"></span>
  <span class="badge" style="left:297px;top:56px;width:110px;height:30px;border-radius:3px"></span>
  <span class="badge" style="left:440px;top:40px;width:80px;height:70px;border-radius:50%;background:#6a6a6a"></span>
  <span class="badge" style="left:564px;top:46px;width:82px;height:46px;border-radius:4px"></span>
</section>

<footer class="abs footer">
  <div class="abs" style="left:123px;top:18px">
    <h4>OUR LOCATION</h4>
    <p>Level 4, Harbour Point<br>22 Cedar Lane<br>MALAYSIA</p>
    <p style="margin-top:9px">Ph: 03-5550-0142<br>Fax: 03-5550-0143</p>
  </div>
  <div class="abs" style="left:341px;top:18px">
    <h4>PRODUCT INFO</h4>
    <ul><li>-Product Warranty</li><li>-Residential Solar Power</li><li>-Commercial Solar Power</li><li>-LED Lightings</li><li>-FAQ</li><li>-Customer Service</li></ul>
  </div>
  <div class="abs" style="left:572px;top:18px">
    <h4>SOCIAL MEDIA</h4>
    <div class="footer-social" style="margin-top:10px"><span></span><span></span><span></span></div>
  </div>
</footer>
<div class="abs footer-bar">
  <span class="abs" style="left:123px">Copyright © 2014 Brightwell Energy</span>
  <span class="abs" style="left:495px">Sitemap &nbsp; - &nbsp; Privacy Policy &nbsp; - &nbsp; Disclaimer</span>
</div>
</body>
</html>
```